Business Card for Makeup Artist

I need a business card designed for my makeup and hair artistry business which is primarily events and weddings focused. The card needs to be sleek, simple, stylish and appealing to women. I would prefer a white background but open to suggestions also. I also love the marble background look. I have attached some example pics. It needs to be a double sided card with logo and/or design on one side and contact details in the centre of the card on the other side. NO LOGO ON BACK. Examples attached.

Target Market(s)

Females age 14-55

Industry/Entity Type

Business

Contact Information for Business Card

Nora Pelling
Principal Makeup Artist
P: 0412 903 251
E: nora@lumivamakeup.com.au
W: www.lumivamakeup.com.au

Requirements
Should not have
• No yellow, green, red or blue in the design.

```html
<!DOCTYPE html>
<html lang="en">
<head>
<meta charset="utf-8">
<title>Nora Pelling – Business Card</title>
<link rel="stylesheet" href="https://fonts.googleapis.com/css2?family=Libre+Bodoni:wght@400&display=swap">
<style>
  :root {
    --ink: #3a3a3c;
    --rose: #d965aa;
    --marble-white: #f5f5f4;
    --marble-light: #ececeb;
    --marble-mid: #dcdddb;
    --marble-grey: #cfd1ce;
  }
  html, body {
    margin: 0;
    padding: 0;
    width: 1200px;
    height: 701px;
    overflow: hidden;
    background: #ffffff;
  }
  .card {
    position: relative;
    width: 1200px;
    height: 701px;
    overflow: hidden;
    font-family: "Libre Bodoni", "Didot", serif;
    font-weight: 400;
    color: var(--ink);
  }
  .card__marble {
    position: absolute;
    inset: 0;
    background:
      linear-gradient(155deg,
        var(--marble-light) 0%,
        var(--marble-white) 22%,
        var(--marble-mid) 38%,
        var(--marble-white) 55%,
        var(--marble-light) 72%,
        var(--marble-grey) 88%,
        var(--marble-light) 100%);
  }
  .card__text {
    position: absolute;
    left: 0;
    width: 100%;
    margin: 0;
    text-align: center;
    line-height: 1;
    white-space: nowrap;
    font-weight: 400;
  }
  .accent { color: var(--rose); }
  .name  { top: 186px; font-size: 110px; }
  .title { top: 305px; font-size: 48px; }
  .phone { top: 432px; font-size: 52px; }
  .email { top: 486px; font-size: 50px; }
  .web   { top: 539px; font-size: 50px; }
</style>
</head>
<body>
  <main class="card">
    <div class="card__marble" role="img" aria-label="White marble background with soft grey veining"></div>
    <h1 class="card__text name">Nora <span class="accent">Pelling</span></h1>
    <p class="card__text title"><span class="accent">Principal</span> Makeup <span class="accent">Artist</span></p>
    <p class="card__text phone">0412 903 251</p>
    <p class="card__text email">nora@lumivamakeup.com.au</p>
    <p class="card__text web">www.lumivamakeup.com.au</p>
  </main>
</body>
</html>
```